Business card design needed

I need a business card for my Sydney Painting Business, that specialises in painting High -end residential homes. i want the design to look clean, modern and edgy. i also want a logo next to the RK Decorating, using RKD together.

Industry/Entity Type

Residential

Contact Information for Business Card

RK Decorating (business name),LIC 581062B, Rob Kellaway, robert.kellaway@fernmail.net, mobile 0412573068

```html
<!DOCTYPE html>
<html lang="en">
<head>
<meta charset="utf-8">
<title>RK Decorating – Business Card</title>
<link rel="stylesheet" href="https://fonts.googleapis.com/css2?family=Source+Sans+3:wght@400;600;700&display=swap">
<style>
  :root {
    --card-bg: #ffffff;
    --card-border: #9d9d9d;
    --ink-black: #0c0c0c;
    --ink-grey: #6d6e70;
    --bullet-light: #d0717a;
    --bullet-mid: #b94a55;
    --bullet-dark: #9b2d33;
    --swatch-silver: #d1d2d4;
    --swatch-red: #c9232a;
    --swatch-orange: #da7a33;
    --swatch-amber: #f2c12f;
    --swatch-yellow: #ede93a;
    --swatch-green: #3fa856;
    --swatch-forest: #2e8c4c;
    --swatch-purple: #8a2a88;
    --swatch-pink: #b85c9f;
    --swatch-blue: #236fb3;
    --swatch-black: #000000;
  }
  html, body {
    margin: 0;
    padding: 0;
    width: 1200px;
    height: 693px;
    overflow: hidden;
    background: var(--card-bg);
  }
  .business-card {
    display: block;
    width: 1200px;
    height: 693px;
    font-family: "Source Sans 3", "Myriad Pro", Arial, sans-serif;
  }
  .card-frame { fill: var(--card-bg); stroke: var(--card-border); stroke-width: 4; }
  .brand-mark { font-weight: 700; font-size: 184px; fill: var(--ink-black); letter-spacing: 2px; }
  .brand-name { font-weight: 600; font-size: 64px; fill: var(--ink-grey); }
  .contact-line { font-weight: 600; font-size: 35px; fill: var(--ink-grey); }
  .contact-mobile { font-weight: 700; font-size: 43px; fill: var(--ink-black); letter-spacing: 0.5px; }
  .bullet-light { fill: var(--bullet-light); }
  .bullet-mid { fill: var(--bullet-mid); }
  .bullet-dark { fill: var(--bullet-dark); }
</style>
</head>
<body>
<svg class="business-card" viewBox="0 0 1200 693" xmlns="http://www.w3.org/2000/svg">
  <rect class="card-frame" x="2" y="2" width="1196" height="689"/>

  <g class="brand-lockup">
    <text class="brand-mark" x="600" y="271" text-anchor="middle">RKD</text>
    <text class="brand-name" x="600" y="336" text-anchor="middle">RK Decorating</text>
  </g>

  <g class="contact-details">
    <rect class="bullet-light" x="380" y="437" width="18" height="18"/>
    <text class="contact-line" x="401" y="457">LIC 581062B, Rob Kellaway</text>

    <rect class="bullet-mid" x="341" y="480" width="18" height="18"/>
    <text class="contact-line" x="362" y="500">robert.kellaway@fernmail.net</text>

    <rect class="bullet-dark" x="387" y="537" width="20" height="20"/>
    <text class="contact-mobile" x="411" y="559">mobile: 0412573068</text>
  </g>

  <g class="colour-swatches">
    <rect x="143" y="578" width="64" height="64" fill="var(--swatch-silver)"/>
    <rect x="228" y="578" width="64" height="64" fill="var(--swatch-red)"/>
    <rect x="314" y="578" width="64" height="64" fill="var(--swatch-orange)"/>
    <rect x="399" y="578" width="64" height="64" fill="var(--swatch-amber)"/>
    <rect x="484" y="578" width="64" height="64" fill="var(--swatch-yellow)"/>
    <rect x="569" y="578" width="64" height="64" fill="var(--swatch-green)"/>
    <rect x="655" y="578" width="64" height="64" fill="var(--swatch-forest)"/>
    <rect x="740" y="578" width="64" height="64" fill="var(--swatch-purple)"/>
    <rect x="825" y="578" width="64" height="64" fill="var(--swatch-pink)"/>
    <rect x="910" y="578" width="64" height="64" fill="var(--swatch-blue)"/>
    <rect x="994" y="578" width="64" height="64" fill="var(--swatch-black)"/>
  </g>
</svg>
</body>
</html>
```